Communications Contractor Business Card Design

I would like a new business card for a new Communications company in Australia. Subcontracting and specialising in cabling, data, phone, antennas, pay tv ,modems, audio visual fibre optics etc. I am open to colour and design concepts but would like a modern clean look that stands out.

Industry/Entity Type

Tv

Contact Information for Business Card

kestrel communications pty ltd, Doug Pemberton, PO BOX 657 Marlow Flats QLD 4873 kestrel4me@maildrop-example.com Australia. ph 0437196084. Director/Technician. services- Cabling,data,phone,antennas,audio visual,home theatre, fibre optics.

```html
<!DOCTYPE html>
<html lang="en">
<head>
<meta charset="utf-8">
<title>Kestrel Communications – Business Card</title>
<link rel="stylesheet" href="https://fonts.googleapis.com/css2?family=Noto+Sans:wght@400;600;700&display=swap">
<style>
  :root {
    --brand-blue: #1f5ba8;
    --ink-blue: #1a56a6;
    --ink-grey: #555a60;
    --band-grey: #6b6d70;
    --card-white: #ffffff;
    --card-shade: #eef0f2;
    --backdrop: #d9dadc;
  }
  * { box-sizing: border-box; margin: 0; padding: 0; }
  html, body {
    width: 1200px;
    height: 1037px;
    overflow: hidden;
    background: var(--backdrop);
    font-family: "Noto Sans", Verdana, sans-serif;
  }
  .sheet {
    width: 1200px;
    height: 1037px;
    display: flex;
    flex-direction: column;
    align-items: center;
    justify-content: center;
    gap: 30px;
  }
  .card {
    position: relative;
    width: 800px;
    height: 480px;
    overflow: hidden;
    box-shadow: 0 6px 18px rgba(0,0,0,0.18);
  }

  /* Back of card */
  .card-back {
    background: var(--brand-blue);
    color: var(--card-white);
    text-align: center;
  }
  .name-plate {
    position: absolute;
    left: 250px;
    top: 0;
    width: 300px;
    height: 150px;
    background: linear-gradient(180deg, #ffffff 0%, #eceef0 100%);
    border-radius: 0 0 10px 10px;
    display: flex;
    align-items: center;
    justify-content: center;
    padding: 0 24px;
  }
  .name-plate .company-name {
    font-size: 27px;
    font-weight: 600;
    line-height: 1.2;
    color: var(--ink-blue);
  }
  .services-title {
    position: absolute;
    top: 205px;
    width: 100%;
    font-size: 26px;
    font-weight: 400;
  }
  .services-list {
    position: absolute;
    top: 265px;
    width: 100%;
    font-size: 19px;
    line-height: 1.45;
  }

  /* Front of card */
  .card-front {
    background: linear-gradient(90deg, var(--card-white) 0%, var(--card-white) 55%, var(--card-shade) 100%);
  }
  .front-brand {
    position: absolute;
    left: 36px;
    top: 40px;
    font-size: 36px;
    font-weight: 600;
    color: var(--ink-blue);
  }
  .contact-person {
    position: absolute;
    left: 36px;
    top: 140px;
  }
  .contact-person .person-name {
    font-size: 24px;
    font-weight: 700;
    color: var(--ink-grey);
  }
  .contact-person .person-role {
    font-size: 18px;
    color: var(--ink-blue);
  }
  .contact-lines {
    position: absolute;
    left: 36px;
    top: 250px;
    list-style: none;
    font-size: 19px;
    color: var(--ink-grey);
    line-height: 1.6;
  }
  .contact-lines li { display: flex; align-items: center; gap: 10px; }
  .contact-lines svg { width: 18px; height: 18px; fill: var(--ink-blue); flex: none; }
  .postal {
    position: absolute;
    right: 36px;
    top: 318px;
    text-align: right;
  }
  .postal .postal-company {
    font-size: 21px;
    color: var(--ink-blue);
    margin-bottom: 4px;
  }
  .postal .postal-address {
    font-size: 22px;
    color: var(--ink-grey);
    line-height: 1.15;
  }
  .footer-bands {
    position: absolute;
    left: 0;
    bottom: 0;
    width: 800px;
    height: 100px;
  }
  .footer-bands .band-blue { fill: var(--brand-blue); }
  .footer-bands .band-grey { fill: var(--band-grey); }
</style>
</head>
<body>
<main class="sheet">

  <section class="card card-back" aria-label="Business card back">
    <div class="name-plate">
      <span class="company-name">kestrel communications pty ltd</span>
    </div>
    <h2 class="services-title">Service</h2>
    <p class="services-list">
      Data | Phone | Cabling | Antennas<br>
      Fibre optics | Audio visual | Home theatre
    </p>
  </section>

  <section class="card card-front" aria-label="Business card front">
    <h1 class="front-brand">kestrel communications pty ltd</h1>

    <div class="contact-person">
      <p class="person-name">Doug Pemberton</p>
      <p class="person-role">Director/Technician</p>
    </div>

    <ul class="contact-lines">
      <li>
        <svg viewBox="0 0 24 24" aria-hidden="true"><path d="M6.6 10.8a15.1 15.1 0 0 0 6.6 6.6l2.2-2.2c.3-.3.7-.4 1-.2 1.1.4 2.3.6 3.6.6.6 0 1 .4 1 1V20c0 .6-.4 1-1 1C10.6 21 3 13.4 3 4c0-.6.4-1 1-1h3.5c.6 0 1 .4 1 1 0 1.3.2 2.5.6 3.6.1.3 0 .7-.2 1z"/></svg>
        <span>043.719.6084</span>
      </li>
      <li>
        <svg viewBox="0 0 24 24" aria-hidden="true"><path d="M2 5h20v14H2zM4 7v.4l8 5 8-5V7zm0 2.8V17h16V9.8l-8 5z"/></svg>
        <span>kestrel4me@maildrop-example.com</span>
      </li>
    </ul>

    <div class="postal">
      <p class="postal-company">kestrel communications pty ltd</p>
      <p class="postal-address">PO BOX 657 Marlow<br>Flats QLD 4873</p>
    </div>

    <svg class="footer-bands" viewBox="0 0 800 100" aria-hidden="true">
      <path class="band-blue" d="M0 8 L470 78 L470 100 L0 100 Z"/>
      <path class="band-grey" d="M360 100 C385 70 420 58 470 58 L800 58 L800 100 Z"/>
      <path fill="#ffffff" d="M0 30 L360 100 L0 100 Z"/>
    </svg>
  </section>

</main>
</body>
</html>
```